Corvin Aviation - Learn to Fly

Our customers are people who span all ages and genders that are interested in learning how to fly airplanes for fun or as a career, or who would like to advance their piloting skills.

Flight training we offer:
Private Pilot Certificate
Instrument Rating
Commercial Pilot Certificate
Sport Pilot Certificate: Powered Parachute
Drone Pilot Training

Ground School we offer:
Sport Pilot Ground School
Private Pilot Ground School
Instrument Pilot Ground School
Drone Pilot Ground School

Target Market(s)

Bessemer, Alabama, United States: High school students, college students, career changers. Someone interested in learning to fly for fun or for a career in the United States.

Industry/Entity Type

Aviation

Requirements
Must have
• I would like for you to enjoy some creative freedom here. The feeling and image we want to portray is a professional, but also very exciting and energizing image. The prospective customer and student should see the brochure and be excited to call us or come out for more information on learning how to fly. Our tag line is: "Small Step Today, Giant Leap Tomorrow."
Nice to have
• It would be helpful if you can do some reading or a little research on each of the types of training that we offer so that you will understand what should be included in the brochure. Our goal is to let everyone know who we are, what we offer, and how to contact us.

This may help some with design ideas: The name Corvin Aviation is inspired by the Lystra Orbital Program because the owner of the flight school is a big fan of ORVEX and the Corvin mission.

```html
<!DOCTYPE html>
<html lang="en">
<head>
<meta charset="utf-8">
<title>Corvin Aviation – Learn to Fly</title>
<link href="https://fonts.googleapis.com/css2?family=Kanit:ital,wght@1,800&family=Barlow+Condensed:ital,wght@0,600;1,700&family=Barlow:wght@600&display=swap" rel="stylesheet">
<style>
  :root {
    --sky-top: #17ace6;
    --sky-mid: #4fc1ee;
    --sky-low: #a8dcf3;
    --paper: #f3f4f6;
    --navy: #121f33;
    --navy-deep: #0c1629;
    --red: #e41e26;
    --white: #ffffff;
  }
  * { margin: 0; padding: 0; box-sizing: border-box; }
  html, body { width: 970px; height: 1200px; overflow: hidden; background: var(--paper); }
  .flyer { position: relative; width: 970px; height: 1200px; background: var(--paper); overflow: hidden; }
  .sky {
    position: absolute; left: 0; top: 0; width: 970px; height: 642px;
    background:
      radial-gradient(ellipse 320px 180px at 860px 110px, rgba(255,255,255,.55), transparent 70%),
      radial-gradient(ellipse 260px 160px at 120px 60px, rgba(255,255,255,.45), transparent 70%),
      linear-gradient(180deg, var(--sky-top) 0%, var(--sky-mid) 55%, var(--sky-low) 100%);
  }
  .brand {
    position: absolute; left: 66px; top: 56px; width: 300px; height: 294px;
    border-radius: 50%; background: var(--navy);
    display: flex; align-items: center; justify-content: center; text-align: center;
  }
  .brand-name {
    font-family: "Kanit", sans-serif; font-style: italic; font-weight: 800;
    color: var(--white); font-size: 40px; line-height: 1.05;
  }
  .headline { position: absolute; right: 55px; top: 70px; text-align: right; font-family: "Kanit", sans-serif; font-style: italic; font-weight: 800; }
  .headline span { display: block; line-height: 1; }
  .tag-small { color: var(--white); font-size: 80px; text-shadow: 3px 4px 0 rgba(18,31,51,.85); text-transform: lowercase; }
  .tag-today { color: var(--navy); font-size: 148px; margin-top: -8px; }
  .tag-leap { color: var(--white); font-size: 90px; text-shadow: 3px 4px 0 rgba(18,31,51,.85); margin-top: 8px; }
  .tag-tomorrow { color: var(--navy); font-size: 148px; margin-top: -2px; margin-right: -4px; }
  .rule-red { position: absolute; left: 0; top: 638px; width: 970px; height: 7px; background: var(--red); }
  .photo { position: absolute; top: 530px; width: 285px; height: 182px; border: 3px solid var(--white); }
  .photo-1 { left: 34px; background: linear-gradient(180deg, #8793ad 0%, #5d6b8c 45%, #3a4a6d 100%); }
  .photo-2 { left: 343px; background: linear-gradient(180deg, #c9c0a6 0%, #8a8466 40%, #465232 75%, #2e3a22 100%); }
  .photo-3 { left: 650px; background: linear-gradient(180deg, #4d6276 0%, #274763 40%, #123553 100%); }
  .col { position: absolute; top: 740px; }
  .col-flight { left: 81px; }
  .col-ground { left: 512px; }
  .col-title { font-family: "Barlow Condensed", sans-serif; font-style: italic; font-weight: 700; color: var(--red); font-size: 50px; line-height: 1; text-transform: uppercase; }
  .col-sub { font-family: "Barlow Condensed", sans-serif; font-weight: 600; color: var(--red); font-size: 34px; line-height: 1; margin-top: 6px; }
  .col-rule { width: 306px; height: 3px; background: var(--navy); margin-top: 10px; margin-bottom: 8px; }
  .col ul { list-style: none; }
  .col li { font-family: "Barlow Condensed", sans-serif; font-weight: 600; color: var(--navy); font-size: 29px; line-height: 36px; padding-left: 26px; position: relative; }
  .col li::before { content: ""; position: absolute; left: 0; top: 12px; width: 14px; height: 14px; border-radius: 50%; background: var(--navy); }
  .footer-rule { position: absolute; left: 0; top: 1109px; width: 970px; height: 7px; background: var(--red); }
  .footer { position: absolute; left: 0; top: 1116px; width: 970px; height: 84px; background: linear-gradient(90deg, var(--navy-deep), #15244a 50%, var(--navy-deep)); display: flex; align-items: center; justify-content: center; }
  .contact { font-family: "Barlow", sans-serif; font-weight: 600; color: var(--white); font-size: 34px; }
</style>
</head>
<body>
<main class="flyer">
  <section class="sky"></section>

  <div class="brand"><span class="brand-name">Corvin<br>Aviation</span></div>

  <h1 class="headline">
    <span class="tag-small">small step</span>
    <span class="tag-today">TODAY</span>
    <span class="tag-leap">GIANT LEAP</span>
    <span class="tag-tomorrow">TOMORROW</span>
  </h1>

  <div class="rule-red"></div>
  <div class="photo photo-1" role="img" aria-label="Photo of a white high-wing training plane flying over hills"></div>
  <div class="photo photo-2" role="img" aria-label="Photo of a low-wing light aircraft on grass at sunset"></div>
  <div class="photo photo-3" role="img" aria-label="Photo of a white plane flying over a lake with a bridge"></div>

  <section class="col col-flight">
    <h2 class="col-title">Flight Training</h2>
    <p class="col-sub">WE OFFER:</p>
    <div class="col-rule"></div>
    <ul>
      <li>Private Pilot Certificate</li>
      <li>Instrument Rating</li>
      <li>Commercial Pilot Certificate</li>
      <li>Sport Pilot Certificate</li>
      <li>Powered Parachute</li>
      <li>Drone Pilot Training</li>
    </ul>
  </section>

  <section class="col col-ground">
    <h2 class="col-title">Ground School</h2>
    <p class="col-sub">WE OFFER:</p>
    <div class="col-rule"></div>
    <ul>
      <li>Sport Pilot Ground School</li>
      <li>Private Pilot Ground School</li>
      <li>Instrument Pilot Ground School</li>
      <li>Drone Pilot Ground School</li>
    </ul>
  </section>

  <div class="footer-rule"></div>
  <footer class="footer">
    <p class="contact">Ph: 0145 872 3306 | www.corvinaviation.com</p>
  </footer>
</main>
</body>
</html>
```